Art Business Needs a Wordpress Theme

I need a Wordpress theme for my company, Fen Ru Haven. Fen Ru stands for Love, Local and the company's focus is to increase awareness of local art and artists. The site will have a blog with posts that showcase local art, art how-to techniques, featured artists and art events. These could be broken down into separate pages or just kept within the homepage. I have a logo that I would like to incorporate. The only request I will make about the layout is that it can feature pictures prominently. Eventually with the help of a Pledgewell campaign I would like to turn the site into an upscale e-commerce platform for member artists of the site. The blog that you are designing will be built on as the business grows into its full vision.

Target Market(s)

Young professionals, Art fans and home designers

Industry/Entity Type

Business

Number of Pages Required

3 page

Font styles to use
Sans Serif

Colors
eda3c7
e667a6
e34197
f59195
f04a50
f68d4d
f37122

Requirements
Must have
• An about page and a contact page. I would like it if the logo was featured on the top left of the screen along with the words Love. Local. Art.
Nice to have
• Perhaps if possible it would be cool to have a way for people to enter their email if they were interested in joining a mailing list or having the Social media information displayed on a sidebar.

```html
<!DOCTYPE html>
<html lang="en">
<head>
<meta charset="utf-8">
<title>Fen Ru Haven</title>
<link href="https://fonts.googleapis.com/css2?family=Noto+Serif:wght@700&family=Open+Sans:wght@400;600;700&display=swap" rel="stylesheet">
<style>
:root{
  --paper:#f4eadc;
  --paper-edge:#eadbc6;
  --card:#ffffff;
  --ink:#2b2622;
  --muted:#8d8780;
  --pink:#e34197;
  --pink-soft:#eda3c7;
  --rose:#e667a6;
  --line:#e6ddd1;
  --pill:#f1ede8;
  --footer:#1f1c1a;
}
*{box-sizing:border-box;margin:0;padding:0}
html,body{width:761px;height:1200px;overflow:hidden}
body{
  position:relative;
  font-family:"Open Sans",Arial,sans-serif;
  color:var(--ink);
  background:radial-gradient(ellipse at 55% 35%,#f8f0e5 0%,var(--paper) 55%,var(--paper-edge) 100%);
}
/* Sidebar */
.sidebar{position:absolute;left:38px;top:14px;width:150px}
.brand{display:flex;flex-direction:column;align-items:flex-start}
.brand-mark{width:58px;height:58px;border-radius:50%;background:var(--pink-soft);margin-left:10px}
.brand-name{margin-top:8px;font-size:15px;font-weight:700;color:var(--ink)}
.brand-tagline{font-size:8px;color:var(--muted);letter-spacing:.5px;margin-top:1px}
.main-nav{list-style:none;margin-top:34px}
.main-nav li{font-size:8.5px;font-weight:600;color:var(--pink);letter-spacing:.6px;height:22px;display:flex;align-items:center}
.main-nav li::before{content:"";width:7px;height:1px;background:var(--pink);margin-right:6px}
.social{display:flex;gap:5px;margin-top:18px}
.social span{width:14px;height:14px;background:#7d7873;border-radius:2px}
.widget-title{font-size:7.5px;font-weight:700;color:var(--pink);letter-spacing:.5px;margin-top:22px}
.subscribe{margin-top:8px;width:120px;height:18px;border:1px solid var(--line);background:#fff;font-size:7px;color:#b2aaa1;padding:0 6px;display:flex;align-items:center;justify-content:space-between}
.subscribe i{width:6px;height:6px;border-top:1px solid #b2aaa1;border-right:1px solid #b2aaa1;transform:rotate(45deg)}
.popular{list-style:none;margin-top:10px}
.popular li{display:flex;gap:6px;margin-bottom:13px}
.popular li::before{content:"";flex:none;width:6px;height:1px;background:var(--pink);margin-top:5px}
.popular h4{font-size:7px;line-height:10px;color:var(--rose);font-weight:600}
.popular p{font-size:6px;line-height:9px;color:var(--muted);margin-top:2px}
/* Posts */
.post{position:absolute;left:208px;width:498px;height:242px;background:var(--card);box-shadow:0 1px 3px rgba(80,60,40,.15);display:flex;padding:10px}
.post-image{flex:none;width:128px;height:100%}
.post-body{padding:4px 0 0 14px}
.post-title{font-family:"Noto Serif",Georgia,serif;font-size:11px;line-height:15px;font-weight:700;color:var(--ink);width:300px}
.post-meta{display:flex;gap:5px;margin-top:12px;margin-bottom:14px}
.post-meta span{font-size:6.5px;color:var(--muted);background:var(--pill);border:1px solid var(--line);padding:3px 7px}
.post-meta .icon{width:18px;padding:0;display:flex;align-items:center;justify-content:center}
.post-excerpt{font-size:7.5px;line-height:13px;color:var(--muted);width:330px}
.img-gallery{background:linear-gradient(160deg,#7a958f 0%,#c9c3b3 35%,#d5694a 60%,#5b4b44 100%)}
.img-canal{background:linear-gradient(170deg,#c79a4c 0%,#9aa17c 40%,#4f7f86 70%,#3f3a2e 100%)}
.img-portrait{background:linear-gradient(160deg,#e9e3d6 0%,#d8b59a 45%,#b84c5a 70%,#4f6fa8 100%)}
.img-paint{background:linear-gradient(150deg,#1b1010 0%,#8d1620 45%,#d8323a 65%,#2a0c0c 100%)}
/* Pagination */
.pagination{position:absolute;left:214px;top:1102px;display:flex;gap:8px}
.pagination span{width:14px;height:14px;border-radius:50%;border:1px solid #b8b0a6;background:#fff;font-size:6.5px;color:var(--muted);display:flex;align-items:center;justify-content:center}
.pagination .current{background:#7a7c8a;border-color:#7a7c8a;color:#fff}
/* Footer */
.site-footer{position:absolute;left:0;top:1166px;width:761px;height:34px;background:var(--footer);color:#bdb5ab;font-size:6.5px;display:flex;align-items:center;justify-content:center}
</style>
</head>
<body>
<aside class="sidebar">
  <div class="brand">
    <span class="brand-mark"></span>
    <span class="brand-name">Fen Ru Haven</span>
    <span class="brand-tagline">Love. Local. Art.</span>
  </div>
  <ul class="main-nav">
    <li>HOME</li><li>ABOUT</li><li>ART</li><li>CONTACT</li>
  </ul>
  <div class="social"><span></span><span></span><span></span></div>
  <div class="widget-title">NEWSLETTER SUBSCRIBE</div>
  <div class="subscribe">Email<i></i></div>
  <div class="widget-title">POPULAR ARTICLES</div>
  <ul class="popular">
    <li><div><h4>Donec vestibulum odio sem, ac laoreet massa</h4><p>Nullam quis risus eget urna mollis ornare vel eu leo.</p></div></li>
    <li><div><h4>Donec vestibulum odio sem, ac laoreet massa</h4><p>Nullam quis risus eget urna mollis ornare vel eu leo.</p></div></li>
    <li><div><h4>Donec vestibulum odio sem, ac laoreet massa</h4><p>Nullam quis risus eget urna mollis ornare vel eu leo.</p></div></li>
  </ul>
</aside>

<article class="post" style="top:38px">
  <div class="post-image img-gallery" role="img" aria-label="Photo of a visitor viewing colourful paintings in a gallery"></div>
  <div class="post-body">
    <h2 class="post-title">Donec vestibulum odio sem, ac laoreet massa ullamcorper porttitor turpis venenatis luctus</h2>
    <div class="post-meta"><span>May 14, 2014</span><span>Admin</span><span>12 Comments</span><span class="icon"><svg width="8" height="7" viewBox="0 0 8 7"><path d="M0 0h8v5H3L1 7V5H0z" fill="#8d8780"/></svg></span></div>
    <p class="post-excerpt">Nullam quis risus eget urna mollis ornare vel eu leo. Cras mattis consectetur purus sit amet fermentum. Maecenas faucibus mollis interdum. Donec ullamcorper nulla non metus auctor fringilla. Vivamus sagittis lacus vel augue laoreet rutrum faucibus dolor auctor. Aenean lacinia bibendum nulla sed consectetur. Etiam porta sem malesuada magna mollis euismod. Praesent commodo cursus magna, vel scelerisque nisl consectetur et.</p>
  </div>
</article>

<article class="post" style="top:300px">
  <div class="post-image img-canal" role="img" aria-label="Painted scene of a canal with a bridge and old buildings"></div>
  <div class="post-body">
    <h2 class="post-title">Donec vestibulum odio sem, ac laoreet massa ullamcorper porttitor turpis venenatis luctus</h2>
    <div class="post-meta"><span>May 14, 2014</span><span>Admin</span><span>12 Comments</span><span class="icon"><svg width="8" height="7" viewBox="0 0 8 7"><path d="M0 0h8v5H3L1 7V5H0z" fill="#8d8780"/></svg></span></div>
    <p class="post-excerpt">Nullam quis risus eget urna mollis ornare vel eu leo. Cras mattis consectetur purus sit amet fermentum. Maecenas faucibus mollis interdum. Donec ullamcorper nulla non metus auctor fringilla. Vivamus sagittis lacus vel augue laoreet rutrum faucibus dolor auctor. Aenean lacinia bibendum nulla sed consectetur. Etiam porta sem malesuada magna mollis euismod. Praesent commodo cursus magna, vel scelerisque nisl consectetur et.</p>
  </div>
</article>

<article class="post" style="top:564px">
  <div class="post-image img-portrait" role="img" aria-label="Photo of an artist holding a bunch of colourful paper flowers"></div>
  <div class="post-body">
    <h2 class="post-title">Donec vestibulum odio sem, ac laoreet massa ullamcorper porttitor turpis venenatis luctus</h2>
    <div class="post-meta"><span>May 14, 2014</span><span>Admin</span><span>12 Comments</span><span class="icon"><svg width="8" height="7" viewBox="0 0 8 7"><path d="M0 0h8v5H3L1 7V5H0z" fill="#8d8780"/></svg></span></div>
    <p class="post-excerpt">Nullam quis risus eget urna mollis ornare vel eu leo. Cras mattis consectetur purus sit amet fermentum. Maecenas faucibus mollis interdum. Donec ullamcorper nulla non metus auctor fringilla. Vivamus sagittis lacus vel augue laoreet rutrum faucibus dolor auctor. Aenean lacinia bibendum nulla sed consectetur. Etiam porta sem malesuada magna mollis euismod. Praesent commodo cursus magna, vel scelerisque nisl consectetur et.</p>
  </div>
</article>

<article class="post" style="top:828px">
  <div class="post-image img-paint" role="img" aria-label="Photo of bold red body paint art on a dark background"></div>
  <div class="post-body">
    <h2 class="post-title">Donec vestibulum odio sem, ac laoreet massa ullamcorper porttitor turpis venenatis luctus</h2>
    <div class="post-meta"><span>May 14, 2014</span><span>Admin</span><span>12 Comments</span><span class="icon"><svg width="8" height="7" viewBox="0 0 8 7"><path d="M0 0h8v5H3L1 7V5H0z" fill="#8d8780"/></svg></span></div>
    <p class="post-excerpt">Nullam quis risus eget urna mollis ornare vel eu leo. Cras mattis consectetur purus sit amet fermentum. Maecenas faucibus mollis interdum. Donec ullamcorper nulla non metus auctor fringilla. Vivamus sagittis lacus vel augue laoreet rutrum faucibus dolor auctor. Aenean lacinia bibendum nulla sed consectetur. Etiam porta sem malesuada magna mollis euismod. Praesent commodo cursus magna, vel scelerisque nisl consectetur et.</p>
  </div>
</article>

<nav class="pagination">
  <span class="current">1</span><span>2</span><span>3</span><span>4</span><span>5</span><span>6</span><span>7</span>
</nav>

<footer class="site-footer">Copyright © 2014 · Fen Ru Haven · All rights reserved.</footer>
</body>
</html>
```